Lumora business card for a plastic surgeon

we need a business card for plastic surgeons that work on a clinic called LUMORA.
we want a clean design and the following informations: name of the doctor, doctor's registration number (called CRM), telephone, address, facebook, instagram.
Colors: white, blue tones, light brown/ coffee

facebook and instagram: lumoraesteticaclinica

Industry/Entity Type

Business

Contact Information for Business Card

clean design

Font styles to use
Serif
Sans Serif
Other font styles liked:
• helvetica light

Colors
cee9f5
85cae6
85abd2
3276b5
cfeae6
cedeed
eaf1f7

Requirements
Must have
• doctor's name
• identification number (called CRM)
• contact (phone, facebook, instagram, address)

```html
<!DOCTYPE html>
<html lang="pt">
<head>
<meta charset="utf-8">
<title>Lumora – Business Card</title>
<link rel="stylesheet" href="https://fonts.googleapis.com/css2?family=Cormorant+Garamond:wght@500&family=EB+Garamond:wght@400&display=swap">
<style>
  :root {
    --stage: #e6e9ec;
    --paper: #ffffff;
    --cyan: #2bb5d5;
    --band: #2cc0dc;
    --navy: #1d3f6d;
    --ink: #5a5f66;
    --shadow: rgba(20, 30, 45, 0.18);
  }
  * { margin: 0; padding: 0; box-sizing: border-box; }
  html, body { width: 1200px; height: 950px; overflow: hidden; }
  body {
    background: var(--stage);
    display: flex;
    flex-direction: column;
    align-items: center;
    justify-content: center;
    gap: 50px;
    font-family: "EB Garamond", Georgia, serif;
  }
  .card {
    position: relative;
    width: 700px;
    height: 400px;
    background: var(--paper);
    box-shadow: 0 10px 30px var(--shadow);
    overflow: hidden;
  }
  .brand {
    display: flex;
    align-items: center;
    gap: 14px;
    font-family: "Cormorant Garamond", Georgia, serif;
    font-weight: 500;
    color: var(--cyan);
    letter-spacing: 6px;
    line-height: 1;
  }
  .brand-dot {
    width: 14px; height: 14px;
    border-radius: 50%;
    background: var(--cyan);
  }

  /* back side */
  .card-back {
    display: flex;
    flex-direction: column;
    align-items: center;
    justify-content: center;
    gap: 26px;
  }
  .card-back .brand { font-size: 78px; }
  .social {
    display: flex;
    align-items: center;
    gap: 10px;
    color: var(--ink);
    font-size: 19px;
    letter-spacing: 0.3px;
  }
  .social-dot {
    width: 16px; height: 16px;
    border-radius: 3px;
    background: var(--navy);
  }

  /* front side */
  .card-front .brand {
    position: absolute;
    left: 160px;
    top: 58px;
    font-size: 66px;
  }
  .contact {
    position: absolute;
    left: 70px;
    top: 172px;
    list-style: none;
    color: var(--ink);
    font-size: 18px;
    line-height: 25px;
  }
  .contact li { display: flex; align-items: flex-start; gap: 14px; }
  .contact svg { width: 16px; height: 16px; margin-top: 4px; flex: none; fill: var(--cyan); }
  .contact .lines { display: flex; flex-direction: column; }

  .doctor {
    position: absolute;
    right: 0;
    bottom: 48px;
    width: 300px;
    height: 72px;
    background: var(--band);
    color: var(--paper);
    padding: 8px 0 0 82px;
    font-size: 23px;
    line-height: 28px;
  }
  .doctor-badge {
    position: absolute;
    left: -46px;
    top: 50%;
    transform: translateY(-50%);
    width: 96px; height: 96px;
    border-radius: 50%;
    background: var(--navy);
    border: 4px solid var(--paper);
  }
</style>
</head>
<body>

  <section class="card card-back" aria-label="Verso do cartão">
    <div class="brand"><span class="brand-dot"></span>LUMORA</div>
    <div class="social"><span class="social-dot"></span>lumoraesteticaclinica</div>
  </section>

  <section class="card card-front" aria-label="Frente do cartão">
    <div class="brand"><span class="brand-dot"></span>LUMORA</div>

    <ul class="contact">
      <li>
        <svg viewBox="0 0 16 16" aria-hidden="true"><path d="M8 0a5.5 5.5 0 0 0-5.5 5.5C2.5 10 8 16 8 16s5.5-6 5.5-10.5A5.5 5.5 0 0 0 8 0zm0 7.6a2.1 2.1 0 1 1 0-4.2 2.1 2.1 0 0 1 0 4.2z"/></svg>
        <span class="lines"><span>2190 Harbor Crest Lane</span><span>Glen Oaks, NY 11004</span></span>
      </li>
      <li>
        <svg viewBox="0 0 16 16" aria-hidden="true"><path d="M3.6 1.2 6 3.6 4.6 5.6c.9 2.2 3.5 4.9 5.8 5.8l2-1.4 2.4 2.4-1.6 2.3C7.7 15.2.8 8.3 1.3 2.8z"/></svg>
        <span>555 0192 4471</span>
      </li>
      <li>
        <svg viewBox="0 0 16 16" aria-hidden="true"><path d="M1 3h14v1.2L8 8.8 1 4.2zm0 2.6 7 4.6 7-4.6V13H1z"/></svg>
        <span>marina@lumora.com</span>
      </li>
      <li>
        <svg viewBox="0 0 16 16" aria-hidden="true"><circle cx="8" cy="8" r="7.5"/><path d="M.5 8h15M8 .5c2.5 2.5 2.5 12.5 0 15M8 .5c-2.5 2.5-2.5 12.5 0 15" stroke="#fff" stroke-width="1" fill="none"/></svg>
        <span>www.lumoraclinic.com</span>
      </li>
    </ul>

    <div class="doctor">
      <span class="doctor-badge"></span>
      <div class="doctor-name">Marina Vale</div>
      <div class="doctor-crm">(CRM)61203</div>
    </div>
  </section>

</body>
</html>
```